Brett Olsen Building Business Card Design

Hi,

I need a business card for my Building company.
I am a Builder and build homes for clients.
I am looking for a sophisticated logo that can be used on business cards, envelopes and letter heads.
I am trying to take my business to the next level and need a professional business card.

Colours: Please use white, black, dark grey and bright blue.

Thank you,

Carol and Brett.

Target Market(s)

1. Home and Building Companies 2. Potential customers

Industry/Entity Type

Business

Contact Information for Business Card

Brett Olsen Building PTY LTD

Brett Olsen

Director

A.B.N. 37 829 516 073

BUILDERS LICENCE No. 573019k

Mobile: 0412 907 381

Email: brettolsenbuilding@mailvane.com.au

Requirements
Must have
• The following is compulsory to have in the designs:

Brett Olsen Building PTY LTD (business name)

Brett Olsen (contact name)

Director (position)

A.B.N. 37 829 516 073

Builders Licence No. 573019k

Mobile: 0412 907 381

Nice to have
• Logo for business
Should not have
• Should not be cluttered.

I am looking for a clean, sophisticated and professional business card design.

```html
<!DOCTYPE html>
<html lang="en">
<head>
<meta charset="utf-8">
<title>Brett Olsen Building – Business Card</title>
<link rel="stylesheet" href="https://fonts.googleapis.com/css2?family=Arimo:wght@400;700&display=swap">
<style>
  :root {
    --page-bg: #e6e7e9;
    --card-bg: #000000;
    --card-edge: #2a2a2a;
    --brand-blue: #1a8fd6;
    --brand-blue-light: #37b4ec;
    --text-white: #ffffff;
    --text-grey: #c4c4c4;
    --pattern-grey: #5a5b5d;
  }
  * { margin: 0; padding: 0; box-sizing: border-box; }
  html, body {
    width: 1200px; height: 900px; overflow: hidden;
    background: var(--page-bg);
    font-family: "Arimo", Arial, sans-serif;
  }
  .card {
    position: absolute; left: 252px; width: 696px; height: 425px;
    background: var(--card-bg);
    border: 1px solid var(--card-edge);
    overflow: hidden;
  }
  .card--front { top: 18px; }
  .card--back { top: 458px; }

  .texture {
    position: absolute; right: 0; top: 0; width: 380px; height: 340px;
    background: radial-gradient(ellipse at 100% 0%, var(--pattern-grey) 0%, #2b2b2c 40%, rgba(0,0,0,0) 75%);
  }

  .brand { position: absolute; display: flex; flex-direction: column; }
  .brand__name {
    display: flex; align-items: center; gap: 12px;
    font-weight: 700; color: var(--brand-blue);
    font-size: 44px; line-height: 1; letter-spacing: -0.5px;
  }
  .brand__mark { width: 34px; height: 34px; background: var(--brand-blue); flex: none; }
  .brand__legal {
    margin-top: 14px; font-weight: 700; color: var(--brand-blue);
    font-size: 21px; line-height: 1;
  }
  .brand__legal small { font-size: 15px; letter-spacing: 0.5px; }

  .card--front .brand { left: 42px; top: 42px; }

  .person { position: absolute; left: 42px; top: 212px; }
  .person__name { font-size: 30px; line-height: 1; color: var(--brand-blue); }
  .person__name strong { color: var(--text-white); font-weight: 700; }
  .person__role { margin-top: 4px; font-size: 22px; color: var(--text-grey); }

  .contact { position: absolute; left: 330px; top: 287px; list-style: none; }
  .contact li {
    position: relative; padding-left: 38px; height: 30px;
    font-size: 18px; line-height: 30px; color: var(--text-grey);
  }
  .contact svg { position: absolute; left: 0; top: 1px; width: 28px; height: 28px; }

  .card--back .brand { left: 0; right: 0; top: 142px; align-items: center; }
  .card--back .brand__legal { margin-top: 22px; }
  .rule {
    position: absolute; left: 176px; top: 267px; width: 348px; height: 4px;
    background: linear-gradient(90deg, rgba(255,255,255,0), #dcdcdc 50%, rgba(255,255,255,0));
  }
</style>
</head>
<body>

<section class="card card--front">
  <div class="texture" role="img" aria-label="Perforated metal texture fading from dark grey to black"></div>

  <div class="brand">
    <div class="brand__name"><span class="brand__mark"></span>Brett Olsen Building</div>
    <div class="brand__legal">Brett Olsen Building <small>PTY LTD</small></div>
  </div>

  <div class="person">
    <div class="person__name"><strong>Brett</strong> Olsen</div>
    <div class="person__role">Director</div>
  </div>

  <ul class="contact">
    <li>
      <svg viewBox="0 0 28 28" aria-hidden="true">
        <circle cx="14" cy="14" r="13" fill="var(--brand-blue)" stroke="#fff" stroke-width="1.5"/>
        <rect x="10" y="7" width="8" height="14" rx="1.5" fill="none" stroke="#fff" stroke-width="1.5"/>
        <line x1="13" y1="18.5" x2="15" y2="18.5" stroke="#fff" stroke-width="1.2"/>
      </svg>0412 907 381
    </li>
    <li>
      <svg viewBox="0 0 28 28" aria-hidden="true">
        <circle cx="14" cy="14" r="13" fill="var(--brand-blue)" stroke="#fff" stroke-width="1.5"/>
        <rect x="7.5" y="9.5" width="13" height="9" fill="none" stroke="#fff" stroke-width="1.5"/>
        <polyline points="7.5,9.5 14,15 20.5,9.5" fill="none" stroke="#fff" stroke-width="1.5"/>
      </svg>brettolsenbuilding@mailvane.com.au
    </li>
    <li>A.B.N. 37 829 516 073</li>
    <li>Builders Licence No. 573019k</li>
  </ul>
</section>

<section class="card card--back">
  <div class="brand">
    <div class="brand__name"><span class="brand__mark"></span>Brett Olsen Building</div>
    <div class="brand__legal">Brett Olsen Building <small>PTY LTD</small></div>
  </div>
  <div class="rule"></div>
</section>

</body>
</html>
```